Biz Cards to match new logo

I'm looking for a business card layout to go with my new logo. I'd like to have one side in colour (purple, with the logo in white) and the other side to be white with the purple logo and contact info in black font: name, address (2 lines), phone, email, fax, website. The logo includes the company name so it doesn't need to be repeated in the text. The font should be legibile to the semi-blind. (I hate small fonts on business cards).

```html
<!DOCTYPE html>
<html lang="en">
<head>
<meta charset="utf-8">
<title>Thalvik Research – Business Cards</title>
<link rel="stylesheet" href="https://fonts.googleapis.com/css2?family=Arimo:wght@700&display=swap">
<style>
  :root {
    --brand-purple: #4f1ec8;
    --card-white: #ffffff;
    --ink-black: #111111;
    --backdrop: #5f5c58;
    --card-shadow: rgba(0, 0, 0, 0.35);
  }
  * { box-sizing: border-box; margin: 0; padding: 0; }
  html, body {
    width: 1200px;
    height: 900px;
    overflow: hidden;
    background: var(--backdrop);
    font-family: "Arimo", Arial, sans-serif;
    font-weight: 700;
  }
  .canvas {
    position: relative;
    width: 1200px;
    height: 900px;
  }
  .card {
    position: absolute;
    width: 600px;
    height: 350px;
    overflow: hidden;
    box-shadow: 0 8px 20px var(--card-shadow);
  }
  .card--front { left: 70px; top: 80px; }
  .card--back  { left: 530px; top: 470px; }
  .card__art {
    position: absolute;
    inset: 0;
    width: 600px;
    height: 350px;
    display: block;
  }
  .wordmark {
    position: absolute;
    left: 44px;
    top: 96px;
    width: 250px;
    line-height: 1;
    text-align: center;
  }
  .wordmark__name {
    display: block;
    font-size: 46px;
    letter-spacing: 3px;
  }
  .wordmark__sub {
    display: block;
    margin-top: 8px;
    font-size: 17px;
    letter-spacing: 7px;
  }
  .card--front .wordmark { color: var(--card-white); }
  .card--back .wordmark { color: var(--brand-purple); }

  .contact {
    position: absolute;
    top: 250px;
    font-size: 19px;
    line-height: 22px;
  }
  .contact--main { left: 28px; }
  .contact--extra { left: 318px; top: 272px; }
  .card--front .contact { color: var(--ink-black); }
  .card--back .contact { color: var(--card-white); }
  .contact__row { display: flex; }
  .contact__label { width: 92px; }
  .contact--extra .contact__label { width: 100px; }
</style>
</head>
<body>
<main class="canvas">

  <section class="card card--front" aria-label="Business card, coloured side">
    <svg class="card__art" viewBox="0 0 600 350" aria-hidden="true">
      <rect x="0" y="0" width="600" height="350" fill="var(--card-white)"/>
      <rect x="0" y="0" width="600" height="240" fill="var(--brand-purple)"/>
      <path d="M356,0 C340,60 306,120 338,172 C364,214 400,236 446,240"
            fill="none" stroke="var(--card-white)" stroke-width="9" stroke-linecap="round"/>
      <g class="search-icon" fill="none" stroke="var(--card-white)" stroke-linecap="round">
        <circle cx="468" cy="68" r="40" stroke-width="13"/>
        <line x1="499" y1="99" x2="548" y2="136" stroke-width="16"/>
      </g>
    </svg>
    <div class="wordmark">
      <span class="wordmark__name">THALVIK</span>
      <span class="wordmark__sub">RESEARCH</span>
    </div>
    <div class="contact contact--main">
      <div class="contact__row"><span class="contact__label">Name</span><span>:</span></div>
      <div class="contact__row"><span class="contact__label">Address</span><span>:</span></div>
      <div class="contact__row"><span class="contact__label">Phone</span><span>:</span></div>
      <div class="contact__row"><span class="contact__label">E-mail</span><span>:</span></div>
    </div>
    <div class="contact contact--extra">
      <div class="contact__row"><span class="contact__label">Fax</span><span>:</span></div>
      <div class="contact__row"><span class="contact__label">Website</span><span>:</span></div>
    </div>
  </section>

  <section class="card card--back" aria-label="Business card, white side">
    <svg class="card__art" viewBox="0 0 600 350" aria-hidden="true">
      <rect x="0" y="0" width="600" height="350" fill="var(--card-white)"/>
      <rect x="0" y="240" width="600" height="110" fill="var(--brand-purple)"/>
      <path d="M356,0 C340,60 306,120 338,172 C364,214 400,236 446,240"
            fill="none" stroke="var(--brand-purple)" stroke-width="9" stroke-linecap="round"/>
      <g class="search-icon" fill="none" stroke="var(--brand-purple)" stroke-linecap="round">
        <circle cx="468" cy="68" r="40" stroke-width="13"/>
        <line x1="499" y1="99" x2="548" y2="136" stroke-width="16"/>
      </g>
    </svg>
    <div class="wordmark">
      <span class="wordmark__name">THALVIK</span>
      <span class="wordmark__sub">RESEARCH</span>
    </div>
    <div class="contact contact--main">
      <div class="contact__row"><span class="contact__label">Name</span><span>:</span></div>
      <div class="contact__row"><span class="contact__label">Address</span><span>:</span></div>
      <div class="contact__row"><span class="contact__label">Phone</span><span>:</span></div>
      <div class="contact__row"><span class="contact__label">E-mail</span><span>:</span></div>
    </div>
    <div class="contact contact--extra">
      <div class="contact__row"><span class="contact__label">Fax</span><span>:</span></div>
      <div class="contact__row"><span class="contact__label">Website</span><span>:</span></div>
    </div>
  </section>

</main>
</body>
</html>
```